Tessaline Bioscience Advisors.

Molecular Technology Consulting. Feasibility, Evaluation and Validation of ISH/IHC and Imaging Applications.

Industry/Entity Type

Consulting

Contact Information for Business Card

Tessaline Bioscience Advisors
Cell: 330 555-0147
Dorian Makepeace
dmakepeace7804@quillmail.test

```html
<!DOCTYPE html>
<html lang="en">
<head>
<meta charset="utf-8">
<title>Tessaline Bioscience Advisors – Business Card</title>
<link rel="stylesheet" href="https://fonts.googleapis.com/css2?family=Exo+2:ital,wght@0,700;1,700&family=Open+Sans:wght@400&display=swap">
<style>
  :root {
    --green: #3fae3a;
    --green-light: #62c24f;
    --green-dark: #1f6b22;
    --green-deep: #174f19;
    --ink: #1c1c1c;
    --paper: #ffffff;
    --stage: #eceeea;
    --rule: #2b2b2b;
  }
  * { box-sizing: border-box; margin: 0; padding: 0; }
  html, body { width: 1200px; height: 784px; overflow: hidden; }
  body {
    background: var(--stage);
    font-family: "Open Sans", Arial, sans-serif;
    position: relative;
  }
  .card {
    position: absolute;
    top: 238px;
    width: 530px;
    height: 308px;
    overflow: hidden;
    box-shadow: 0 6px 18px rgba(0,0,0,0.18);
  }
  .card--back { left: 50px; background: var(--green-dark); }
  .card--front { left: 620px; background: var(--paper); }

  .back-pattern {
    position: absolute; inset: 0;
    background:
      radial-gradient(ellipse at 20% 80%, var(--green-light) 0%, rgba(98,194,79,0) 55%),
      linear-gradient(135deg, var(--green) 0%, var(--green-dark) 55%, var(--green-deep) 100%);
  }

  .brand {
    position: absolute;
    display: flex;
    align-items: center;
    gap: 14px;
    font-family: "Exo 2", Arial, sans-serif;
    font-weight: 700;
    line-height: 1.1;
  }
  .brand__square { flex: none; width: 16px; height: 16px; }
  .brand__name { display: block; }

  .card--back .brand { left: 60px; top: 112px; color: var(--paper); font-size: 30px; }
  .card--back .brand__square { background: var(--paper); }

  .card--front .brand { left: 40px; top: 58px; color: var(--green); font-size: 26px; }
  .card--front .brand__square { background: var(--green); }

  .contact { position: absolute; left: 40px; top: 170px; color: var(--ink); }
  .contact__name {
    color: var(--green);
    font-size: 22px;
    font-weight: 400;
    margin-bottom: 8px;
  }
  .contact__line {
    display: flex; align-items: center; gap: 6px;
    font-size: 17px; line-height: 24px;
  }
  .contact__icon { width: 18px; height: 18px; flex: none; }

  .tagline-band {
    position: absolute; left: 0; right: 0; bottom: 0;
    height: 30px;
    background: var(--green);
    border-top: 3px solid var(--rule);
    display: flex; align-items: center; justify-content: center;
    color: var(--paper);
    font-family: "Exo 2", Arial, sans-serif;
    font-style: italic;
    font-weight: 700;
    font-size: 11.5px;
    letter-spacing: 0.9px;
    text-transform: uppercase;
    white-space: nowrap;
  }
</style>
</head>
<body>

  <section class="card card--back" aria-label="Card back">
    <div class="back-pattern" role="img" aria-label="Green background with a receding pattern of soft light-green ovals"></div>
    <div class="brand">
      <span class="brand__square"></span>
      <span class="brand__name">Tessaline Bioscience<br>Advisors</span>
    </div>
  </section>

  <section class="card card--front" aria-label="Card front">
    <div class="brand">
      <span class="brand__square"></span>
      <span class="brand__name">Tessaline Bioscience<br>Advisors</span>
    </div>

    <div class="contact">
      <p class="contact__name">Dorian Makepeace</p>
      <p class="contact__line">
        <svg class="contact__icon" viewBox="0 0 20 20" aria-hidden="true">
          <circle cx="10" cy="10" r="9" fill="none" stroke="var(--green)" stroke-width="1.6"/>
          <path d="M6.4 5.6l1.8-.4 1 2.3-1.1.8a6 6 0 0 0 3.2 3.2l.8-1.1 2.3 1-.4 1.8c-4 .4-8-3.6-7.6-7.6z" fill="var(--green)"/>
        </svg>
        330 555-0147
      </p>
      <p class="contact__line">
        <svg class="contact__icon" viewBox="0 0 20 20" aria-hidden="true">
          <circle cx="10" cy="10" r="9" fill="none" stroke="var(--green)" stroke-width="1.6"/>
          <rect x="5" y="6.5" width="10" height="7" fill="none" stroke="var(--green)" stroke-width="1.4"/>
          <path d="M5 6.5l5 4 5-4" fill="none" stroke="var(--green)" stroke-width="1.4"/>
        </svg>
        dmakepeace7804@quillmail.test
      </p>
    </div>

    <div class="tagline-band">Feasibility, Evaluation and Validation of ISH/IHC and Imaging Applications.</div>
  </section>

</body>
</html>
```